Full printing package for Fadeel Trading & Maint. Co. Ltd
Business card, email signature, A4 folder & stationary
Full printing package for Fadeel Trading & Maint. Co. Ltd -
Tariq Mardini
Executive Manager
P.O.Box 4582, Riyadh 13872 Kingdom of Saudi Arabia
t.mardini@fadeelco-ksa.com
www.fadeelco-ksa.com
I need two designs for the business card: 1.front side to have name & title in both arabic & English ( address in English only) and on the back side logo & website. 2. One side name ,company name & title in arabic ( address only english) back side name ,company name & title in english. For A4 envelope,letter head,email signature & folder to use same address as business card.

```html
<!DOCTYPE html>
<html lang="en">
<head>
<meta charset="utf-8">
<title>Fadeel Trading &amp; Maint. Co. Ltd – Stationery Package</title>
<link href="https://fonts.googleapis.com/css2?family=Open+Sans:wght@400;600;700&display=swap" rel="stylesheet">
<style>
  :root{
    --orange:#e4562c;
    --blue:#2f5d86;
    --ink:#3a3f47;
    --muted:#8a9099;
    --paper:#ffffff;
    --stage:#eceeef;
    --edge:#d6d9dc;
  }
  *{box-sizing:border-box;margin:0;padding:0}
  html,body{width:1200px;height:310px;overflow:hidden;background:var(--stage);font-family:"Open Sans",Arial,sans-serif;color:var(--ink)}
  .canvas{position:relative;width:1200px;height:310px}
  .sheet{position:absolute;background:var(--paper);border:1px solid var(--edge);box-shadow:0 1px 3px rgba(0,0,0,.12);overflow:hidden}
  .brand{display:flex;align-items:center;gap:4px;color:var(--blue);font-weight:700;line-height:1}
  .brand .dot{border-radius:50%;background:var(--orange);flex:none}

  /* hero lockup */
  .hero{position:absolute;left:30px;top:14px}
  .hero .brand{font-size:44px;gap:10px}
  .hero .dot{width:30px;height:30px}
  .hero .tagline{margin:6px 0 0 42px;color:var(--blue);font-size:17px;font-weight:600}
  .hero .sub{margin:6px 0 0 42px;font-size:6px;color:var(--muted)}

  /* business cards */
  .card{width:113px;height:72px}
  .card .brand{position:absolute;left:7px;top:7px;font-size:10px}
  .card .brand .dot{width:7px;height:7px}
  .card .lines{position:absolute;right:7px;top:10px;text-align:right;font-size:3.6px;line-height:1.55;color:var(--ink)}
  .card .lines strong{display:block;font-size:5px;color:var(--orange)}
  .card .strip{position:absolute;left:0;right:0;bottom:0;height:5px;background:var(--blue)}
  .card .strip::before{content:"";position:absolute;left:0;top:0;bottom:0;width:35%;background:var(--orange)}
  .card .company{position:absolute;left:7px;top:30px;font-size:5px;font-weight:700;color:var(--orange)}
  .card .person{position:absolute;left:7px;top:40px;font-size:3.8px;line-height:1.5}
  .card .center{position:absolute;left:0;right:0;top:24px;display:flex;flex-direction:column;align-items:center}
  .card .center .brand{position:static;font-size:12px}
  .card .center .brand .dot{width:8px;height:8px}
  .card .center .url{margin-top:5px;font-size:3.6px;color:var(--muted)}

  /* letterheads */
  .letter{width:174px;height:282px;top:12px}
  .letter .brand{position:absolute;left:10px;top:10px;font-size:10px}
  .letter .brand .dot{width:7px;height:7px}
  .letter .contact{position:absolute;right:10px;top:11px;font-size:3.3px;line-height:1.6;text-align:left;color:var(--muted)}
  .letter .halo{position:absolute;left:62px;top:118px;width:50px;height:50px;border-radius:50%;background:var(--orange);opacity:.12}
  .letter .foot{position:absolute;left:10px;right:10px;bottom:10px;text-align:center;font-size:3.3px;color:var(--muted);line-height:1.6}
  .letter .rule{position:absolute;left:0;right:0;bottom:0;height:3px;background:var(--blue)}
  .letter .rule::before{content:"";position:absolute;left:0;top:0;bottom:0;width:40%;background:var(--orange)}

  /* compliment slips */
  .slip{left:696px;width:192px}
  .slip .brand{position:absolute;left:9px;top:9px;font-size:10px}
  .slip .brand .dot{width:7px;height:7px}
  .slip .contact{position:absolute;right:9px;top:10px;font-size:3.4px;line-height:1.6;color:var(--muted)}
  .slip .rule{position:absolute;left:0;right:0;bottom:0;height:4px;background:var(--blue)}
  .slip .rule::before{content:"";position:absolute;left:0;top:0;bottom:0;width:40%;background:var(--orange)}
  .slip .halo{position:absolute;left:20px;top:36px;width:34px;height:34px;border-radius:50%;background:var(--orange);opacity:.12}
  .slip .foot{position:absolute;left:0;right:0;bottom:8px;text-align:center;font-size:3.3px;color:var(--muted)}

  /* envelopes */
  .envelope{position:absolute;left:900px;width:288px;box-shadow:0 1px 3px rgba(0,0,0,.15)}
  .envelope svg{display:block}
  .envelope .brand{position:absolute;left:12px;top:10px;font-size:11px}
  .envelope .brand .dot{width:8px;height:8px}
  .envelope .addr{position:absolute;left:12px;top:26px;font-size:3.4px;color:var(--muted);line-height:1.6}
</style>
</head>
<body>
<main class="canvas">

  <section class="hero">
    <div class="brand"><span class="dot"></span>Fadeel</div>
    <p class="tagline">Safety &amp; Security</p>
    <p class="sub">Fadeel Trading &amp; Maint. Co. Ltd</p>
  </section>

  <!-- business cards -->
  <article class="sheet card" style="left:12px;top:113px">
    <div class="brand"><span class="dot"></span>Fadeel</div>
    <div class="lines" style="top:30px">
      <strong>Tariq Mardini</strong>
      Executive Manager<br>
      T +966 11 400 2210<br>
      M +966 50 318 7745<br>
      t.mardini@fadeelco-ksa.com
    </div>
    <div class="strip"></div>
  </article>

  <article class="sheet card" style="left:132px;top:113px">
    <div class="brand"><span class="dot"></span>Fadeel</div>
    <div class="lines" style="top:30px">
      <strong>Tariq Mardini</strong>
      P.O.Box 4582, Riyadh 13872<br>
      Kingdom of Saudi Arabia<br>
      F +966 11 400 2211<br>
      www.fadeelco-ksa.com
    </div>
    <div class="strip"></div>
  </article>

  <article class="sheet card" style="left:12px;top:197px">
    <div class="brand"><span class="dot"></span>Fadeel</div>
    <p class="company">Fadeel Trading &amp; Maint. Co. Ltd</p>
    <p class="person">Tariq Mardini<br>Executive Manager<br>t.mardini@fadeelco-ksa.com</p>
    <div class="strip"></div>
  </article>

  <article class="sheet card" style="left:132px;top:197px">
    <div class="center">
      <div class="brand"><span class="dot"></span>Fadeel</div>
      <p class="url">www.fadeelco-ksa.com</p>
    </div>
    <div class="strip"></div>
  </article>

  <!-- letterheads -->
  <article class="sheet letter" style="left:264px">
    <div class="brand"><span class="dot"></span>Fadeel</div>
    <div class="contact">T +966 11 400 2210<br>F +966 11 400 2211<br>P.O.Box 4582, Riyadh 13872<br>www.fadeelco-ksa.com</div>
    <div class="halo"></div>
    <p class="foot">Fadeel Trading &amp; Maint. Co. Ltd · P.O.Box 4582, Riyadh 13872<br>www.fadeelco-ksa.com</p>
    <div class="rule"></div>
  </article>

  <article class="sheet letter" style="left:468px">
    <div class="halo"></div>
    <p class="foot">Fadeel Trading &amp; Maint. Co. Ltd · P.O.Box 4582, Riyadh 13872<br>www.fadeelco-ksa.com</p>
    <div class="rule"></div>
  </article>

  <!-- compliment slips -->
  <article class="sheet slip" style="top:113px;height:67px">
    <div class="brand"><span class="dot"></span>Fadeel</div>
    <div class="contact">T +966 11 400 2210<br>P.O.Box 4582, Riyadh 13872<br>www.fadeelco-ksa.com</div>
    <div class="rule"></div>
  </article>

  <article class="sheet slip" style="top:186px;height:95px">
    <div class="brand"><span class="dot"></span>Fadeel</div>
    <div class="halo"></div>
    <p class="foot">P.O.Box 4582, Riyadh 13872 · www.fadeelco-ksa.com</p>
    <div class="rule"></div>
  </article>

  <!-- envelopes -->
  <div class="envelope" style="top:96px;height:72px">
    <svg width="288" height="72" viewBox="0 0 288 72" aria-hidden="true">
      <rect width="288" height="72" fill="var(--orange)"/>
      <path d="M0 0 L144 34 L288 0" fill="none" stroke="#fff" stroke-opacity=".6" stroke-width="1"/>
    </svg>
  </div>

  <div class="envelope" style="top:128px;height:82px">
    <svg width="288" height="82" viewBox="0 0 288 82" aria-hidden="true">
      <rect width="288" height="82" fill="#f7f8f9"/>
      <path d="M0 0 H288 L144 40 Z" fill="var(--blue)"/>
      <path d="M0 82 L144 40 L288 82" fill="none" stroke="var(--edge)" stroke-width="1"/>
    </svg>
  </div>

  <div class="envelope" style="top:182px;height:95px;background:var(--paper)">
    <svg width="288" height="95" viewBox="0 0 288 95" aria-hidden="true">
      <rect width="288" height="95" fill="var(--paper)"/>
      <rect y="91" width="115" height="4" fill="var(--orange)"/>
      <rect x="115" y="91" width="173" height="4" fill="var(--blue)"/>
    </svg>
    <div class="brand"><span class="dot"></span>Fadeel</div>
    <p class="addr">P.O.Box 4582, Riyadh 13872<br>Kingdom of Saudi Arabia</p>
  </div>

</main>
</body>
</html>
```